Need stationery and business card design for Appraisal Company
Stonewell Valuations & Advisory
Professional
Lonny Harwick
Certified Residential Appraiser
5182 W Maple Ct.
Gilbert, AZ 85234
lonny@stonewellvaluations.example
Business logo and font will be uploaded.

```html
<!DOCTYPE html>
<html lang="en">
<head>
<meta charset="utf-8">
<title>Stonewell Valuations &amp; Advisory — Stationery</title>
<link rel="stylesheet" href="https://fonts.googleapis.com/css2?family=Cinzel:wght@700&family=Open+Sans:wght@400;600&display=swap">
<style>
  :root{
    --bg:#f1f1f1;
    --paper:#ffffff;
    --charcoal:#3a3a3c;
    --charcoal-deep:#222224;
    --ember:#e5471f;
    --ember-light:#f37a2c;
    --ember-deep:#b8261a;
    --ink:#4a4a4a;
    --muted:#9a9a9a;
    --shadow:0 2px 5px rgba(0,0,0,.18);
  }
  *{box-sizing:border-box;margin:0;padding:0}
  html,body{width:1200px;height:322px;overflow:hidden;background:var(--bg)}
  body{position:relative;font-family:"Open Sans",Arial,sans-serif;color:var(--ink)}
  .piece{position:absolute;background:var(--paper);box-shadow:var(--shadow);overflow:hidden}
  .brand{font-family:"Cinzel",Georgia,serif;font-weight:700;color:var(--ember);letter-spacing:.04em;line-height:1.15;display:flex;align-items:flex-start;gap:4px}
  .brand .mark{display:inline-block;background:var(--ember);flex:none;margin-top:1px}
  .brand .name{min-width:0}
  .brand.on-dark{color:var(--ember-light)}
  .brand.on-dark .mark{background:var(--ember-light)}
  .tiny{font-size:3.2px;line-height:1.45;color:var(--ink)}
  .rule{position:absolute;left:0;right:0;height:2px;background:linear-gradient(90deg,var(--ember-deep),var(--ember-light))}

  /* left column */
  .standalone-brand{position:absolute;left:14px;top:98px;width:168px;font-size:9px}
  .standalone-brand .mark{width:9px;height:9px}
  .card-front{left:12px;top:140px;width:168px;height:58px}
  .card-front .brand{position:absolute;left:8px;top:8px;font-size:6px}
  .card-front .brand .mark{width:6px;height:6px;margin-top:0}
  .card-front .who{position:absolute;right:8px;top:26px;text-align:right;font-size:5px;line-height:1.35}
  .card-front .who b{font-weight:600;color:var(--charcoal);display:block;font-size:6px}
  .card-front .rule{bottom:0}
  .card-back{left:12px;top:206px;width:168px;height:106px;background:var(--charcoal-deep)}
  .card-back .brand{position:absolute;left:0;right:0;top:48px;justify-content:center;font-size:7px}
  .card-back .brand .mark{width:7px;height:7px;margin-top:0}

  /* letterhead */
  .letterhead{left:192px;top:12px;width:205px;height:300px}
  .letterhead .brand{position:absolute;left:14px;top:12px;font-size:6.5px;width:110px}
  .letterhead .brand .mark{width:7px;height:7px}
  .letterhead .contact{position:absolute;right:12px;top:12px;text-align:right}
  .letterhead .body{position:absolute;left:14px;top:46px;right:14px}
  .letterhead .body p{margin-bottom:4px}
  .letterhead .sign{position:absolute;left:14px;top:236px}
  .letterhead .sign .line{width:40px;height:1px;background:var(--muted);margin:8px 0 3px}
  .letterhead .rule{bottom:10px;left:14px;right:14px;height:1px}

  /* compliment slip & small card */
  .slip{left:403px;top:96px;width:127px;height:42px}
  .slip .brand{position:absolute;left:7px;top:7px;font-size:4.5px}
  .slip .brand .mark{width:5px;height:5px;margin-top:0}
  .slip .tiny{position:absolute;left:7px;bottom:6px}
  .slip .rule{bottom:0;height:1.5px}
  .mini-card{left:537px;top:100px;width:62px;height:36px}
  .mini-card .brand{position:absolute;left:5px;top:6px;font-size:3.6px}
  .mini-card .brand .mark{width:4px;height:4px;margin-top:0}
  .mini-card .tiny{position:absolute;left:5px;bottom:5px}

  /* envelopes */
  .env-dark{left:617px;top:96px;width:175px;height:48px;background:var(--charcoal)}
  .env-dark .flap{position:absolute;inset:0}
  .env-dark .brand{position:absolute;left:0;right:0;top:22px;justify-content:center;font-size:5px}
  .env-dark .brand .mark{width:5px;height:5px;margin-top:0}
  .env-flap{left:617px;top:150px;width:175px;height:47px;background:var(--paper)}
  .env-front{left:617px;top:203px;width:175px;height:47px}
  .env-front .brand{position:absolute;left:8px;top:7px;font-size:4.5px}
  .env-front .brand .mark{width:5px;height:5px;margin-top:0}
  .env-front .tiny{position:absolute;left:8px;top:16px}
  .env-front .rule{bottom:0;height:1.5px}

  /* large sheet */
  .sheet{left:403px;top:190px;width:197px;height:122px}
  .sheet .brand{position:absolute;left:0;right:0;top:54px;justify-content:center;font-size:8px;color:#f2e4df}
  .sheet .brand .mark{width:8px;height:8px;background:#f2e4df;margin-top:0}
  .sheet .rule{bottom:0;height:1.5px}

  /* presentation folder */
  .folder{left:804px;top:12px;width:384px;height:300px;background:transparent;box-shadow:none;overflow:visible}
  .folder .cover{position:absolute;left:0;top:0;width:190px;height:300px;background:radial-gradient(ellipse at 55% 45%,var(--ember-light) 0%,var(--ember) 55%,var(--ember-deep) 100%);box-shadow:var(--shadow)}
  .folder .cover .brand{position:absolute;left:0;right:0;top:140px;justify-content:center;font-size:9px;color:#fde3d6}
  .folder .cover .brand .mark{width:9px;height:9px;background:#fde3d6;margin-top:0}
  .folder .inside{position:absolute;left:190px;top:0;width:190px;height:300px;background:var(--paper);box-shadow:var(--shadow)}
  .folder .inside .brand{position:absolute;left:14px;top:128px;font-size:10px;width:165px}
  .folder .inside .brand .mark{width:10px;height:10px}
  .folder .inside .tiny{position:absolute;left:14px;bottom:18px;color:var(--muted)}
  .folder .pocket{position:absolute;left:190px;top:200px;width:190px;height:100px;background:linear-gradient(180deg,var(--ember),var(--ember-deep));clip-path:polygon(0 14%,78% 0,100% 10%,100% 100%,0 100%)}
  .folder .tab{position:absolute;right:-4px;top:210px;width:10px;height:70px;background:var(--ember-deep)}
</style>
</head>
<body>

  <div class="brand standalone-brand"><span class="mark"></span><span class="name">Stonewell Valuations &amp; Advisory</span></div>

  <section class="piece card-front">
    <div class="brand"><span class="mark"></span><span class="name">Stonewell Valuations</span></div>
    <div class="who"><b>Lonny Harwick</b>Certified Residential Appraiser<br>lonny@stonewellvaluations.example</div>
    <div class="rule"></div>
  </section>

  <section class="piece card-back">
    <div class="brand on-dark"><span class="mark"></span><span class="name">Stonewell Valuations</span></div>
  </section>

  <section class="piece letterhead">
    <div class="brand"><span class="mark"></span><span class="name">Stonewell Valuations &amp; Advisory</span></div>
    <div class="contact tiny">5182 W Maple Ct.<br>Gilbert, AZ 85234<br>lonny@stonewellvaluations.example</div>
    <div class="body tiny">
      <p>Dear Client,</p>
      <p>Thank you for choosing our team for your residential appraisal. Our report reflects careful review of the property, recent sales nearby and current market conditions.</p>
      <p>Please reach out with any questions about the findings.</p>
    </div>
    <div class="sign tiny">Sincerely,<div class="line"></div>Lonny Harwick<br>Certified Residential Appraiser</div>
    <div class="rule"></div>
  </section>

  <section class="piece slip">
    <div class="brand"><span class="mark"></span><span class="name">Stonewell Valuations &amp; Advisory</span></div>
    <div class="tiny">5182 W Maple Ct. · Gilbert, AZ 85234</div>
    <div class="rule"></div>
  </section>

  <section class="piece mini-card">
    <div class="brand"><span class="mark"></span><span class="name">Stonewell</span></div>
    <div class="tiny">Lonny Harwick</div>
  </section>

  <section class="piece env-dark">
    <svg class="flap" width="175" height="48" viewBox="0 0 175 48" aria-hidden="true">
      <polygon points="0,0 175,0 87.5,20" fill="#2b2b2d"/>
    </svg>
    <div class="brand on-dark"><span class="mark"></span><span class="name">Stonewell Valuations</span></div>
  </section>

  <section class="piece env-flap">
    <svg width="175" height="47" viewBox="0 0 175 47" aria-hidden="true">
      <defs>
        <linearGradient id="flapFill" x1="0" y1="0" x2="0" y2="1">
          <stop offset="0" stop-color="#f37a2c"/>
          <stop offset="1" stop-color="#b8261a"/>
        </linearGradient>
      </defs>
      <polygon points="0,0 175,0 87.5,26" fill="url(#flapFill)"/>
    </svg>
  </section>

  <section class="piece env-front">
    <div class="brand"><span class="mark"></span><span class="name">Stonewell Valuations &amp; Advisory</span></div>
    <div class="tiny">5182 W Maple Ct.<br>Gilbert, AZ 85234</div>
    <div class="rule"></div>
  </section>

  <section class="piece sheet">
    <div class="brand"><span class="mark"></span><span class="name">Stonewell</span></div>
    <div class="rule"></div>
  </section>

  <section class="piece folder">
    <div class="cover">
      <div class="brand"><span class="mark"></span><span class="name">Stonewell</span></div>
    </div>
    <div class="inside">
      <div class="brand"><span class="mark"></span><span class="name">Stonewell Valuations &amp; Advisory</span></div>
      <div class="tiny">5182 W Maple Ct. · Gilbert, AZ 85234 · lonny@stonewellvaluations.example</div>
    </div>
    <div class="pocket"></div>
    <div class="tab"></div>
  </section>

</body>
</html>
```